Business Card - Apex Wellness

Please use the logo / design elements and font to design a business card that is eye catching and informative. If using "Direct Primary Care" logo element, you don't have to spell it out in the text.

Dr. Brendan Halvik
Apex Wellness - Direct Primary Care
4817 Tillbrook Rd. Suite 305
Fort Smith, AR 72916
Phone: 479-555-0137
ApexWellnessAR.example

```html
<!DOCTYPE html>
<html lang="en">
<head>
<meta charset="utf-8">
<title>Apex Wellness – Business Card</title>
<link rel="stylesheet" href="https://fonts.googleapis.com/css2?family=Montserrat:wght@400;500;600&display=swap">
<style>
  :root {
    --backdrop: #dedede;
    --card: #06142f;
    --ink: #ffffff;
    --accent: #12b1e6;
  }
  * { margin: 0; padding: 0; box-sizing: border-box; }
  html, body { width: 1200px; height: 1200px; overflow: hidden; }
  body {
    background: var(--backdrop);
    font-family: "Montserrat", Arial, sans-serif;
    color: var(--ink);
    position: relative;
  }
  .card {
    position: absolute;
    left: 179px;
    width: 861px;
    height: 496px;
    background: var(--card);
    overflow: hidden;
  }
  .card--front { top: 84px; }
  .card--back { top: 621px; }

  .brand-dot {
    position: absolute;
    left: 404px; top: 172px;
    width: 48px; height: 48px;
    border-radius: 50%;
    background: var(--accent);
  }
  .brand-name {
    position: absolute;
    font-weight: 600;
    white-space: nowrap;
    line-height: 1;
  }
  .card--front .brand-name {
    left: 0; right: 0; top: 248px;
    text-align: center;
    font-size: 62px;
    letter-spacing: -0.5px;
  }
  .brand-tag {
    position: absolute;
    font-weight: 600;
    white-space: nowrap;
    letter-spacing: 0.6px;
  }
  .card--front .brand-tag {
    left: 0; right: 0; top: 332px;
    text-align: center;
    font-size: 17px;
  }
  .card--back .brand-name {
    left: 58px; top: 96px;
    font-size: 40px;
    letter-spacing: -0.4px;
  }
  .card--back .brand-tag {
    left: 58px; top: 149px;
    font-size: 13px;
  }

  .person { position: absolute; left: 464px; top: 88px; }
  .person__name { font-size: 33px; font-weight: 500; line-height: 1; white-space: nowrap; }
  .person__role { font-size: 22px; font-weight: 400; margin-top: 6px; }

  .address {
    position: absolute;
    left: 58px; top: 350px;
    font-size: 20px;
    line-height: 30px;
    font-style: normal;
    white-space: nowrap;
  }
  .contact {
    position: absolute;
    left: 466px; top: 320px;
    right: 48px;
    list-style: none;
    font-size: 20px;
    line-height: 30px;
    letter-spacing: 0.2px;
  }
  .contact li { display: flex; align-items: center; white-space: nowrap; }
  .contact svg { width: 19px; height: 19px; margin-right: 10px; flex: none; }
</style>
</head>
<body>

<section class="card card--front" aria-label="Card front">
  <span class="brand-dot"></span>
  <h1 class="brand-name">Apex Wellness</h1>
  <p class="brand-tag">Direct Primary Care</p>
</section>

<section class="card card--back" aria-label="Card back">
  <p class="brand-name">Apex Wellness</p>
  <p class="brand-tag">Direct Primary Care</p>

  <div class="person">
    <p class="person__name">Dr. Brendan Halvik</p>
    <p class="person__role">Founder</p>
  </div>

  <address class="address">
    4817 Tillbrook Rd. Suite 305<br>
    Fort Smith, AR 72916
  </address>

  <ul class="contact">
    <li>
      <svg viewBox="0 0 24 24" aria-hidden="true"><path fill="#fff" d="M6.6 10.8a15.1 15.1 0 0 0 6.6 6.6l2.2-2.2c.3-.3.7-.4 1-.2 1.1.4 2.3.6 3.6.6.6 0 1 .4 1 1V20c0 .6-.4 1-1 1A17 17 0 0 1 3 4c0-.6.4-1 1-1h3.5c.6 0 1 .4 1 1 0 1.3.2 2.5.6 3.6.1.3 0 .7-.2 1z"/><path fill="none" stroke="#fff" stroke-width="1.8" d="M14 3.5a7 7 0 0 1 6.5 6.5M14 7a3.5 3.5 0 0 1 3 3"/></svg>
      479-555-0137
    </li>
    <li>
      <svg viewBox="0 0 24 24" aria-hidden="true"><rect x="2" y="5" width="20" height="14" fill="#fff"/><path fill="none" stroke="#06142f" stroke-width="1.6" d="M2.5 5.5 12 13l9.5-7.5M2.5 18.5l7-6.5M21.5 18.5l-7-6.5"/></svg>
      info@apexwellnessar.example
    </li>
    <li>
      <svg viewBox="0 0 24 24" aria-hidden="true"><g fill="none" stroke="#fff" stroke-width="1.6"><circle cx="12" cy="12" r="9.5"/><ellipse cx="12" cy="12" rx="4.2" ry="9.5"/><path d="M2.5 12h19M4 7h16M4 17h16"/></g></svg>
      www.ApexWellnessAR.example
    </li>
  </ul>
</section>

</body>
</html>
```